Inspection Company - Commercial Brochure Design

We are looking to finalize our 8 x 11 brochure. We are an industry leader in our space of commercial and home inspections.

We really like the front and back design labeled-

We have made some suggestions for the internal pages-

These are only suggestions for the interior section- The wording should remain the same. The images can be removed / rearranged/ etc. There is full creative freedom for the interior.

Wording for Inside Right Page-
With over 500,000 properties inspected we know how to inspect each building type to maximize a Return On Investment for our clients. . Our Inspectors focus on all the critical building components (structural, roof, electrical, plumbing, air and heating, drainage, etc.), health and safety issues – emergency egress and other potential hazards. We document current condition and any immediate and future repairs that are necessary. When scheduling our team take all details into account building construction type, age, location, and property use into consideration to ensure we are fully prepared to conduct a thorough inspection.

Target Market(s)

Investors- Commercial Real Estate Investors

Industry/Entity Type

Commercial Real Estate Inspections

Requirements
Must have
• Similar branding to our website (https://quorvato.com/tamberlycommercial) (https://tamberlyinspections.com/) and ( the uploaded documents (Commercial report cover sample.JPG & plovenrift_z6se15j73jk0fe9fc2samkecn7_image (1).jpg )
Nice to have
• Must have Brand Logos and Brand Colors- Nice to have creative ideas of displaying the information

```html
<!DOCTYPE html>
<html lang="en">
<head>
<meta charset="utf-8">
<title>Tamberly Group – Repair Pricing &amp; Inspection Tools</title>
<link rel="stylesheet" href="https://fonts.googleapis.com/css2?family=Arimo:wght@400;700&family=Ubuntu:wght@300&display=swap">
<style>
:root{
  --stage:#d1d1d1;
  --paper:#ffffff;
  --navy-dark:#0c2747;
  --navy-mid:#174d80;
  --navy-light:#1d66a6;
  --ink-blue:#1f5c97;
  --line-blue:#2a6aa5;
  --white:#ffffff;
  --badge-fill:rgba(255,255,255,.2);
}
*{box-sizing:border-box;margin:0;padding:0}
html,body{width:1200px;height:719px;overflow:hidden;background:var(--stage)}
body{position:relative;font-family:"Arimo",Arial,sans-serif}
.page{position:absolute;top:12px;width:496px;height:638px;background:var(--paper);box-shadow:0 18px 22px -14px rgba(0,0,0,.45)}
.page--pricing{left:33px}
.page--tools{left:673px}
.masthead{position:absolute;left:0;top:20px;width:100%;height:152px;background:linear-gradient(180deg,var(--navy-dark),var(--navy-light))}
.brand{position:absolute;left:30px;top:22px;display:flex;align-items:center;gap:8px}
.brand__mark{width:56px;height:56px;border:3px solid var(--white);border-radius:50%}
.brand__name{color:var(--white);font-weight:700;font-size:15px;letter-spacing:.5px;margin-top:-20px}
.masthead__title{position:absolute;left:94px;top:58px;color:var(--white);font-size:19px;font-weight:400;white-space:nowrap}
.footer-band{position:absolute;left:0;top:490px;width:100%;height:148px;background:linear-gradient(180deg,var(--navy-dark),var(--navy-light))}
.site{position:absolute;top:105px;color:#e4ecf5;font-family:"Ubuntu",sans-serif;font-weight:300;font-size:13.5px;letter-spacing:1px}

/* pricing table */
.col{position:absolute}
.col__head{height:14px;background:linear-gradient(180deg,var(--navy-dark),var(--navy-light));color:var(--white);font-size:9px;text-align:center;line-height:14px}
.col__body{position:absolute;top:19px;left:0;width:100%;height:262px;border:1.5px solid var(--line-blue);display:flex;flex-direction:column}
.col__body div{flex:1;border-bottom:1px solid var(--line-blue);color:var(--ink-blue);display:flex;align-items:center;white-space:nowrap;overflow:hidden}
.col__body div:last-child{border-bottom:none}
.col--num .col__body div{justify-content:center;font-size:9px}
.col--desc .col__body div{font-size:5.6px;padding-left:6px}
.col--detail .col__body div{font-size:5.6px;padding-left:15px}
.col--price .col__body div{justify-content:center;font-size:8.6px}

/* tools grid */
.tool-grid{position:absolute;left:15px;top:183px;width:286px;height:284px;border:1.5px solid var(--line-blue);display:grid;grid-template-columns:93px 96px 1fr;grid-template-rows:145px 1fr}
.tool{border-right:1.5px solid var(--line-blue);border-bottom:1.5px solid var(--line-blue);position:relative;color:var(--ink-blue);font-size:10.5px;text-align:center;line-height:17px}
.tool:nth-child(3n){border-right:none}
.tool:nth-child(n+4){border-bottom:none}
.tool__photo{position:absolute;left:50%;transform:translateX(-50%);border-radius:6px}
.tool__label{position:absolute;left:0;right:0}
.tool-copy{position:absolute;left:318px;top:188px;width:160px;color:var(--ink-blue);font-size:9.9px;line-height:10.2px}
.tool-copy p{text-indent:16px;margin-bottom:5.6px}
.badge{position:absolute;background:var(--badge-fill)}
.badge--certification{left:199px;top:25px;width:134px;height:64px;border-radius:6px}
.badge--program{left:361px;top:25px;width:92px;height:92px;border-radius:50%}
</style>
</head>
<body>

<section class="page page--pricing">
  <header class="masthead">
    <div class="brand"><span class="brand__mark"></span><span class="brand__name">TAMBERLYGROUP</span></div>
    <h1 class="masthead__title">REPAIR PRICING</h1>
  </header>

  <div class="col col--num" style="left:20px;top:190px;width:27px">
    <div class="col__head"></div>
    <div class="col__body"><div>1</div><div>2</div><div>3</div><div>4</div><div>5</div><div>6</div><div>7</div><div>8</div><div>9</div><div>10</div><div>11</div><div>12</div><div>13</div></div>
  </div>
  <div class="col col--desc" style="left:55px;top:190px;width:199px">
    <div class="col__head">DESCRIPTION</div>
    <div class="col__body">
      <div>TEMPOR NOSTRUD NISI EU EST AMET DOLOR SINT</div>
      <div>CONSEQUAT DESERUNT. EIUSMOD LABORE SIT ESSE</div>
      <div>PARIATUR EXCEPTEUR OCCAECAT SED CILLUM EA DOLORE</div>
      <div>IN CULPA NISI. UT VOLUPTATE UT DUIS AD,</div>
      <div>AUTE ET UT ADIPISICING MAGNA.</div>
      <div>PARIATUR EXCEPTEUR OCCAECAT SED CILLUM EA DOLORE</div>
      <div>IN CULPA NISI. UT VOLUPTATE UT DUIS AD,</div>
      <div>AUTE ET UT ADIPISICING MAGNA.</div>
      <div>CONSEQUAT DESERUNT. EIUSMOD LABORE SIT ESSE</div>
      <div>IN CULPA NISI. UT VOLUPTATE UT DUIS AD,</div>
      <div>AUTE ET UT ADIPISICING MAGNA.</div>
      <div>IN CULPA NISI. UT VOLUPTATE UT DUIS AD,</div>
      <div>PARIATUR EXCEPTEUR OCCAECAT SED CILLUM EA DOLORE</div>
    </div>
  </div>
  <div class="col col--detail" style="left:262px;top:190px;width:132px">
    <div class="col__head">DETAILS</div>
    <div class="col__body">
      <div>AUTE ET UT ADIPISICING MAGNA.</div><div>AUTE ET UT ADIPISICING MAGNA.</div><div>AUTE ET UT ADIPISICING MAGNA.</div><div>AUTE ET UT ADIPISICING MAGNA.</div><div>AUTE ET UT ADIPISICING MAGNA.</div><div>AUTE ET UT ADIPISICING MAGNA.</div><div>AUTE ET UT ADIPISICING MAGNA.</div><div>AUTE ET UT ADIPISICING MAGNA.</div><div>AUTE ET UT ADIPISICING MAGNA.</div><div>AUTE ET UT ADIPISICING MAGNA.</div><div>AUTE ET UT ADIPISICING MAGNA.</div><div>AUTE ET UT ADIPISICING MAGNA.</div><div>AUTE ET UT ADIPISICING MAGNA.</div>
    </div>
  </div>
  <div class="col col--price" style="left:402px;top:190px;width:77px">
    <div class="col__head">PRICE</div>
    <div class="col__body">
      <div>$ 300.00</div><div>$ 300.00</div><div>$ 300.00</div><div>$ 300.00</div><div>$ 300.00</div><div>$ 300.00</div><div>$ 300.00</div><div>$ 300.00</div><div>$ 300.00</div><div>$ 300.00</div><div>$ 300.00</div><div>$ 300.00</div><div>$ 300.00</div>
    </div>
  </div>

  <footer class="footer-band">
    <span class="site" style="left:360px">QUORVATO.COM</span>
  </footer>
</section>

<section class="page page--tools">
  <header class="masthead">
    <div class="brand"><span class="brand__mark"></span><span class="brand__name">TAMBERLYGROUP</span></div>
    <h1 class="masthead__title">PROFESSIONAL INSPECTION TOOL</h1>
  </header>

  <div class="tool-grid">
    <div class="tool">
      <div class="tool__photo" role="img" aria-label="Handheld moisture meter" style="top:8px;width:32px;height:76px;background:linear-gradient(180deg,#5a5f66,#2b2f35)"></div>
      <div class="tool__label" style="top:96px">MOISTURE<br>METER</div>
    </div>
    <div class="tool">
      <div class="tool__photo" role="img" aria-label="Sewer inspection camera with cable reel" style="top:14px;width:76px;height:54px;background:linear-gradient(135deg,#3a3d44,#4f5f8f 60%,#8a8e96)"></div>
      <div class="tool__label" style="top:87px">SEWER<br>CAMERA</div>
    </div>
    <div class="tool">
      <div class="tool__photo" role="img" aria-label="White camera drone" style="top:18px;width:78px;height:46px;background:radial-gradient(ellipse at center,#f2f2f2 30%,#5a5d62 80%)"></div>
      <div class="tool__label" style="top:87px">DRONE<br>PICTURES</div>
    </div>
    <div class="tool">
      <div class="tool__photo" role="img" aria-label="Indoor air quality monitor" style="top:30px;width:78px;height:58px;background:linear-gradient(180deg,#f4f6f8,#d8dde2)"></div>
    </div>
    <div class="tool">
      <div class="tool__photo" role="img" aria-label="Voltage tester pen and outlet tester" style="top:16px;width:70px;height:74px;background:linear-gradient(135deg,#2c2c2c,#e2a233 55%,#e0632a)"></div>
      <div class="tool__label" style="top:100px">ELECTRICAL<br>OUTLET</div>
    </div>
    <div class="tool">
      <div class="tool__photo" role="img" aria-label="Thermal imaging camera" style="top:12px;width:40px;height:84px;background:linear-gradient(180deg,#3a3b3f,#1b1c1f)"></div>
      <div class="tool__label" style="top:100px">THERMAL<br>GUN</div>
    </div>
  </div>

  <div class="tool-copy">
    <p>Ipsum incididunt adipisicing esse proident. Duis, sit, ad commodo quis sed in ad? Non in incididunt mollit est, mollit ex eiusmod incididunt. Voluptate aute sint ut qui minim ut do ea. Ullamco enim ut in mollit et in ex cillum ex aliquip laboris, in esse dolor.</p>
    <p>Ipsum incididunt adipisicing esse proident. Duis, sit, ad commodo quis sed in ad? Non in incididunt mollit est, mollit ex eiusmod incididunt. Voluptate aute sint ut qui minim ut do ea. Ullamco enim ut in mollit et in ex cillum ex aliquip laboris, in esse dolor.</p>
    <p>Ipsum incididunt adipisicing esse proident. Duis, sit, ad commodo quis sed in ad? Non in incididunt mollit est, mollit ex eiusmod incididunt. Voluptate aute sint ut qui minim ut do ea. Ullamco enim ut in mollit et in ex cillum ex aliquip laboris, in esse dolor.</p>
  </div>

  <footer class="footer-band">
    <div class="badge badge--certification" role="img" aria-label="Certification badge"></div>
    <div class="badge badge--program" role="img" aria-label="Discount program badge"></div>
    <span class="site" style="left:358px">QUORVATO.COM</span>
  </footer>
</section>

</body>
</html>
```